Vellorin - Business Cards for a new venture

create business card for a startup classified business dealing in construction materials, the cards need to have a professional look but modern, more serious than playful, one of the samples must include the official font (attached), please explore using the official colors in the company's logo

Target Market(s)

Energy sector

Contact Information for Business Card

Font styles to use
Other font styles liked:
• suissnord

Requirements
Must have
• corporate colors (in logo attached)
Nice to have
• Official font (in one of the samples) font is : suissnord
Should not have
• Cartoonish look

```html
<!DOCTYPE html>
<html lang="en">
<head>
<meta charset="UTF-8">
<title>Vellorin – Business Cards</title>
<link href="https://fonts.googleapis.com/css2?family=Work+Sans:wght@400;500&display=swap" rel="stylesheet">
<style>
  :root {
    --backdrop: #1c1d1f;
    --card: #262729;
    --card-deep: #1f2022;
    --brand-blue: #1d5b98;
    --brand-grey: #a8aaad;
    --ink-light: #f2f2f2;
    --rule: #e6e6e6;
  }
  * { margin: 0; padding: 0; box-sizing: border-box; }
  html, body {
    width: 1200px;
    height: 900px;
    overflow: hidden;
    background: var(--backdrop);
    font-family: "Work Sans", Arial, sans-serif;
  }
  .canvas {
    position: relative;
    width: 1200px;
    height: 900px;
  }
  .card {
    position: absolute;
    left: 270px;
    width: 660px;
    height: 377px;
    background: linear-gradient(135deg, var(--card-deep) 0%, var(--card) 70%, #2d2e31 100%);
    border-bottom: 6px solid var(--brand-blue);
    box-shadow: 0 18px 40px rgba(0,0,0,0.45);
    overflow: hidden;
  }
  .card--front { top: 52px; }
  .card--back { top: 468px; }

  .wordmark {
    display: flex;
    align-items: center;
    gap: 12px;
    color: var(--brand-grey);
    font-weight: 500;
    text-transform: uppercase;
    letter-spacing: 0.18em;
  }
  .wordmark__dot {
    width: 14px;
    height: 14px;
    border-radius: 50%;
    background: var(--brand-blue);
    flex: none;
  }
  .card--front .wordmark {
    position: absolute;
    left: 0; right: 0;
    top: 160px;
    justify-content: center;
    font-size: 36px;
  }
  .card--back .wordmark {
    position: absolute;
    left: 48px;
    top: 160px;
    font-size: 28px;
  }
  .divider {
    position: absolute;
    left: 352px;
    top: 82px;
    width: 2px;
    height: 192px;
    background: var(--rule);
  }
  .contact {
    position: absolute;
    left: 382px;
    top: 82px;
    color: var(--ink-light);
  }
  .contact__name {
    color: var(--brand-blue);
    font-size: 22px;
    font-weight: 500;
    text-transform: uppercase;
    line-height: 1.1;
  }
  .contact__role {
    font-size: 14px;
    margin-top: 2px;
    letter-spacing: 0.03em;
  }
  .contact__address {
    font-size: 14.5px;
    line-height: 1.45;
    margin-top: 18px;
    letter-spacing: 0.03em;
  }
  .contact__list {
    list-style: none;
    margin-top: 12px;
    font-size: 15px;
    letter-spacing: 0.03em;
  }
  .contact__item {
    display: flex;
    align-items: center;
    gap: 10px;
    line-height: 1.5;
  }
  .contact__icon {
    width: 11px;
    height: 11px;
    flex: none;
  }
</style>
</head>
<body>
<main class="canvas">

  <section class="card card--front" aria-label="Business card front">
    <div class="wordmark">
      <span class="wordmark__dot"></span>
      <span class="wordmark__name">Vellorin</span>
    </div>
  </section>

  <section class="card card--back" aria-label="Business card back">
    <div class="wordmark">
      <span class="wordmark__dot"></span>
      <span class="wordmark__name">Vellorin</span>
    </div>

    <div class="divider"></div>

    <div class="contact">
      <p class="contact__name">Daniel Hart</p>
      <p class="contact__role">Director</p>
      <p class="contact__address">48 Harrow Lane, Unit 3,<br>Kestrel Bay, PO 20417</p>
      <ul class="contact__list">
        <li class="contact__item">
          <svg class="contact__icon" viewBox="0 0 12 12"><path d="M2.5 1 L4.5 1 L5.2 3.4 L4 4.4 Q5 6.8 7.6 8 L8.6 6.8 L11 7.5 L11 9.5 Q11 11 9.5 11 Q1 10 1 2.5 Q1 1 2.5 1 Z" fill="var(--brand-blue)"/></svg>
          <span>+330 5812-4407</span>
        </li>
        <li class="contact__item">
          <svg class="contact__icon" viewBox="0 0 12 12"><rect x="0.8" y="2.3" width="10.4" height="7.4" fill="none" stroke="var(--brand-blue)" stroke-width="1.2"/><path d="M1 2.6 L6 6.4 L11 2.6" fill="none" stroke="var(--brand-blue)" stroke-width="1.2"/></svg>
          <span>info@vellorin.com</span>
        </li>
        <li class="contact__item">
          <svg class="contact__icon" viewBox="0 0 12 12"><circle cx="6" cy="6" r="5" fill="none" stroke="var(--brand-blue)" stroke-width="1.2"/><ellipse cx="6" cy="6" rx="2.2" ry="5" fill="none" stroke="var(--brand-blue)" stroke-width="1"/><path d="M1 6 H11" stroke="var(--brand-blue)" stroke-width="1"/></svg>
          <span>www.vellorin.com</span>
        </li>
      </ul>
    </div>
  </section>

</main>
</body>
</html>
```